Dale Hargrove Photography New Veltra Car

(3/4 of the Car) Car Wrap. Please can I have the Chatterly and Picstream symbol on the design plus my mobile number 0461837294. I am thinking using Matt Charcoal black with off white text. The Orange on the Car is permanent. You may want to use the orange somewhere as it might match the Car details. ?? Just a thought.

Colors
f37122

Requirements
Must have
• I guess i want the Car to look very slice and professional. I am going to use a Matt Charcoal Grey wrap as a BASE.
Should not have
• Don't want images of Camera or lenses etc. Minimal the Better.

```html
<!DOCTYPE html>
<html lang="en">
<head>
<meta charset="utf-8">
<title>Dale Hargrove Photographer – Vehicle Wrap</title>
<link rel="stylesheet" href="https://fonts.googleapis.com/css2?family=Montserrat:wght@300&family=Open+Sans:wght@400&display=swap">
<style>
  :root {
    --charcoal-light: #6a6b6d;
    --charcoal-mid: #3a3b3d;
    --matt-black: #151516;
    --off-white: #e4e2de;
    --soft-grey: #cfcfcf;
    --orange: #f37122;
    --page: #f2f2f2;
  }
  * { margin: 0; padding: 0; box-sizing: border-box; }
  html, body { width: 1200px; height: 606px; overflow: hidden; background: var(--page); }
  .wrap-panel {
    position: relative;
    width: 1200px;
    height: 606px;
    background: linear-gradient(90deg, var(--charcoal-light) 0%, var(--charcoal-mid) 38%, var(--matt-black) 62%);
    overflow: hidden;
  }
  .swoosh { position: absolute; inset: 0; }
  .brand {
    position: absolute;
    left: 110px;
    top: 300px;
    width: 560px;
    text-align: center;
    font-family: "Montserrat", sans-serif;
    font-weight: 300;
    color: var(--off-white);
  }
  .brand-mark {
    display: block;
    width: 14px;
    height: 14px;
    margin: 0 auto 36px;
    background: var(--off-white);
  }
  .brand-name {
    font-size: 38px;
    letter-spacing: 0.16em;
    white-space: nowrap;
  }
  .brand-role {
    font-size: 20px;
    letter-spacing: 0.2em;
    margin-top: 22px;
  }
  .contact {
    position: absolute;
    right: 70px;
    top: 110px;
    text-align: right;
  }
  .phone {
    font-family: "Open Sans", sans-serif;
    font-size: 40px;
    letter-spacing: 0.06em;
    color: var(--soft-grey);
  }
  .social {
    margin-top: 14px;
    display: flex;
    justify-content: flex-end;
    gap: 18px;
    font-family: "Open Sans", sans-serif;
    font-size: 16px;
    color: var(--orange);
  }
  .social-item { display: flex; align-items: center; gap: 6px; white-space: nowrap; }
  .social-dot { width: 14px; height: 14px; border-radius: 50%; background: var(--orange); }
</style>
</head>
<body>
  <main class="wrap-panel">
    <svg class="swoosh" width="1200" height="606" viewBox="0 0 1200 606" aria-hidden="true">
      <path d="M815 0 C790 200 740 420 640 606 L1200 606 L1200 0 Z" fill="var(--matt-black)"/>
      <path d="M815 0 C790 200 740 420 640 606" fill="none" stroke="var(--orange)" stroke-width="7"/>
      <path d="M760 330 C730 450 700 540 672 606" fill="none" stroke="var(--orange)" stroke-width="7"/>
    </svg>

    <section class="brand">
      <span class="brand-mark"></span>
      <p class="brand-name">DALE HARGROVE</p>
      <p class="brand-role">PHOTOGRAPHER</p>
    </section>

    <section class="contact">
      <p class="phone">0461837294</p>
      <div class="social">
        <span class="social-item"><span class="social-dot"></span>Chatterly</span>
        <span class="social-item"><span class="social-dot"></span>Picstream</span>
      </div>
    </section>
  </main>
</body>
</html>
```